Meridale Family Law Firm Website Renovation

We need a website redesign in SquareSpace that is more modern, user friendly, on brand, less cluttered, easier to navigate, conveys clearly what our services are, and has clear, visible calls to action.

We would like to hire and work with the winning designer to complete the remaining pages of the site.

Target Market(s)

Couples looking for divorce representation or mediation who have a conscious, progressive mindset. They are self-aware and personal development plays an important role in their lives. They want an amicable interaction and aspire to have a healthy relationship after divorce.

Age range: 30-60
Income 100K+ household

Industry/Entity Type

Family Law

Font styles to use
Sans Serif

Colors
85acd3
33a6d7
50c0af
a0cd3a

Requirements
Must have
• Please see attached doc for full creative brief details.

"Changing the way people divorce" on top of site.
Images that show happy clients and that represent males and females. Diversity inclusion is also be important.
We are looking for warm, welcoming design and imagery.
Should not have
• Not heavily attorney focused.
Please see attached brief for full description.

```html
<!DOCTYPE html>
<html lang="en">
<head>
<meta charset="utf-8">
<title>Meridale Family Law &amp; Mediation</title>
<link href="https://fonts.googleapis.com/css2?family=Questrial&family=Lato:wght@400;700&display=swap" rel="stylesheet">
<style>
:root{
  --blue:#33a6d7;
  --teal:#50c0af;
  --teal-dark:#45a991;
  --green:#a0cd3a;
  --soft-blue:#85acd3;
  --navy-btn:#4a6d9c;
  --ink:#222;
  --body:#555;
  --white:#fff;
  --grey:#ececec;
}
*{box-sizing:border-box;margin:0;padding:0}
html,body{width:1200px;height:4132px;overflow:hidden}
body{position:relative;background:var(--white);font-family:"Lato",sans-serif;color:var(--ink)}
.abs{position:absolute}
.heading{font-family:"Questrial",sans-serif;font-weight:400;line-height:1.18}
.btn{position:absolute;display:flex;align-items:center;justify-content:center;font-family:"Lato",sans-serif;font-size:12px;color:var(--white)}
.btn-dark{background:#1f1f1f}
.photo{position:absolute}

/* top bar */
.topbar{top:0;left:0;width:1200px;height:38px;font-size:12px;color:#222}
.topbar span{position:absolute;top:12px}
.topbar b{font-size:14px}

/* nav */
.nav{top:38px;left:0;width:1200px;height:73px;background:var(--blue)}
.brand{position:absolute;display:flex;align-items:center;gap:12px}
.brand-dot{width:52px;height:52px;border-radius:50%;background:var(--white);opacity:.9}
.brand-name{font-family:"Lato",sans-serif;font-size:14px;letter-spacing:3px;line-height:1.25;color:var(--white)}
.nav-links{position:absolute;left:521px;top:28px;display:flex;gap:18px;font-size:12px;color:var(--white)}

/* hero: warm office scene with three laughing clients */
.hero{top:111px;left:0;width:1200px;height:527px;
  background:
    radial-gradient(ellipse 160px 190px at 680px 190px,rgba(214,170,138,.85),rgba(214,170,138,0)),
    radial-gradient(ellipse 150px 180px at 1010px 150px,rgba(150,100,70,.85),rgba(150,100,70,0)),
    radial-gradient(ellipse 130px 160px at 820px 210px,rgba(200,160,128,.8),rgba(200,160,128,0)),
    linear-gradient(180deg,rgba(0,0,0,0) 55%,rgba(32,44,70,.85) 80%,rgba(28,36,56,.95) 100%),
    linear-gradient(100deg,#3a2c22 0%,#6a4f3c 30%,#9a7d66 55%,#cfc6bd 80%,#ece8e2 100%)}
.hero-card{position:absolute;left:95px;top:114px;width:343px;height:300px;background:var(--white);padding:78px 0 0 40px}
.hero-card h1{font-size:29px;color:#333}
.hero-card p{margin-top:14px;font-size:11px;line-height:18px;color:var(--body)}
.hero-card .btn{left:46px;top:208px;width:186px;height:31px;background:var(--blue);font-size:12px}

/* service panels */
.panel{top:638px;height:296px;color:#1d3a36}
.panel-med{left:0;width:589px;background:var(--teal)}
.panel-law{left:589px;width:611px;background:var(--teal-dark)}
.panel h2{position:absolute;top:54px;font-size:27px;color:#1f3f3a}
.panel p{position:absolute;top:128px;width:265px;font-size:12.5px;line-height:17px;color:#1f3f3a}
.panel .btn{width:81px;height:26px;font-size:11px}

/* about */
.about-text{top:1050px;left:256px;width:374px;text-align:center}
.about-text h2{font-size:27px;color:#222}
.about-text p{margin-top:14px;font-size:13px;line-height:21.5px;color:var(--body)}
.about-photo{left:650px;top:996px;width:414px;height:366px;
  background:
    radial-gradient(ellipse 90px 120px at 175px 140px,rgba(236,214,186,.95),rgba(236,214,186,0)),
    radial-gradient(ellipse 120px 110px at 180px 300px,rgba(40,48,70,.9),rgba(40,48,70,0)),
    linear-gradient(110deg,#1c2233 0%,#3d4250 25%,#b7a48f 45%,#6a5a52 65%,#201a1c 100%)}

/* awards */
.awards{top:1460px;left:242px;width:711px;height:228px;border:2px solid #222}
.awards h2{position:absolute;top:-14px;left:82px;width:546px;background:var(--white);text-align:center;font-size:24px;color:#333}
.badge{position:absolute;top:85px}

/* attorneys */
.team-title{top:1778px;left:245px;font-size:26px;color:#222}
.arrow{top:1798px;width:25px;height:24px;background:#111}
.attorney{top:1859px;width:170px;height:183px;
  background:
    radial-gradient(ellipse 45px 58px at 85px 78px,rgba(196,148,118,.95),rgba(196,148,118,0)),
    linear-gradient(180deg,#eceef0 0%,#d9dadc 30%,#b9a08e 55%,#2d3c58 82%,#22304a 100%)}
.att-name{top:2062px;width:190px;text-align:center;font-weight:700;font-size:14px;color:#222}
.att-role{top:2083px;width:190px;text-align:center;font-size:11.5px;color:#666}
.quiz{top:1819px;left:634px;width:319px;height:276px;background:var(--blue);color:var(--white);padding:48px 0 0 45px}
.quiz h2{font-size:24px}
.quiz p{margin-top:10px;width:235px;font-size:12px;line-height:18px}
.quiz .btn{position:absolute;left:45px;top:191px;width:182px;height:32px;background:#1f1f1f}

/* contact block */
.scene{top:2199px;left:363px;width:463px;height:260px;
  background:linear-gradient(180deg,#5f87b8 0%,#9cb8d6 25%,#d6dde3 38%,#8d9aa6 46%,#b49a62 55%,#a3864f 75%,#6e5733 100%)}
.scene-caption{top:2386px;left:363px;width:463px;text-align:center;font-family:"Lato",sans-serif;font-weight:700;font-size:25px;line-height:32px;color:#3f8fd0}
.call-box{top:2376px;left:237px;width:307px;height:454px;background:var(--green);color:var(--white)}
.call-box h2{position:absolute;left:44px;top:200px;font-size:24px;color:#f2f8e2}
.call-box .phone{position:absolute;left:42px;top:270px;font-family:"Questrial",sans-serif;font-weight:700;font-size:27px}
.call-box .btn{left:44px;top:317px;width:199px;height:34px;border:2px solid var(--white);font-weight:700;font-size:11.5px}
.form-box{top:2459px;left:544px;width:656px;height:371px;background:var(--soft-blue);color:var(--white)}
.form-box h2{position:absolute;left:46px;top:84px;font-size:21px}
.form-box .sub{position:absolute;left:46px;top:114px;font-size:12px}
.field{position:absolute;border:1px solid #dde8f4;border-radius:4px;font-size:10px;color:#eef4fb;padding:8px 14px}
.send{left:46px;top:286px;width:348px;height:27px;background:var(--navy-btn);border-radius:3px;font-size:13px}

/* video + about firm */
.video-title{top:2934px;left:266px;font-size:18px;color:#222}
.video{top:3000px;left:265px;width:300px;height:173px;
  background:
    radial-gradient(ellipse 45px 55px at 150px 75px,rgba(205,160,130,.9),rgba(205,160,130,0)),
    radial-gradient(ellipse 80px 60px at 150px 160px,rgba(180,110,200,.8),rgba(180,110,200,0)),
    linear-gradient(135deg,#1b1b1b 0%,#2f3a52 50%,#1b1b1b 100%)}
.video-bar{position:absolute;left:10px;top:12px;font-size:11px;color:var(--white)}
.play{position:absolute;left:130px;top:70px;width:40px;height:30px;border-radius:6px;background:rgba(0,0,0,.75)}
.divider{top:2928px;left:595px;width:2px;height:296px;background:#222}
.firm-brand{top:2948px;left:619px}
.firm-brand .brand-dot{width:52px;height:52px;background:#3b8a5d;opacity:1}
.firm-brand .brand-name{color:#2d2d2d;font-size:12.5px}
.firm h3{top:3016px;left:626px;font-size:17px;color:#222}
.firm p{top:3050px;left:626px;width:310px;font-size:11px;font-style:italic;line-height:17.5px;color:#555}

/* testimonials */
.testimonials{top:3285px;left:0;width:1200px;height:552px;background:var(--blue);overflow:hidden}
.ring{position:absolute;border-radius:50%;border:38px solid rgba(255,255,255,.14)}
.testimonials h2{position:absolute;left:289px;top:108px;font-size:26px;color:var(--white)}
.outline-btn{left:836px;top:125px;width:165px;height:36px;border:2px solid var(--white);font-size:12px}
.quote{top:199px;height:214px;background:var(--white);padding:34px 28px;font-size:10.5px;font-style:italic;line-height:16.3px;color:#666}
.quote::after{content:"";position:absolute;left:70px;bottom:-16px;border-left:16px solid transparent;border-right:16px solid transparent;border-top:16px solid var(--white)}
.client{top:437px;font-family:"Questrial",sans-serif;font-size:15px;color:var(--white)}

/* footer */
.footer{top:3837px;left:18px;width:1182px;height:238px;background:var(--grey)}
.f-title{position:absolute;top:65px;font-family:"Questrial",sans-serif;font-size:14px;color:#222}
.f-list{position:absolute;top:93px;font-size:10px;line-height:17.3px;color:#333;font-weight:700;list-style:none}
.copyright{top:4098px;left:290px;font-size:10.5px;color:#333}
.social{top:4087px;width:28px;height:28px;border-radius:50%;border:2px solid var(--blue)}
</style>
</head>
<body>

<header class="abs topbar">
  <span style="left:252px">Schedule for free consultation &nbsp;<b>(555) 014-2290</b></span>
  <span style="left:608px">For any query mailus at &nbsp;<b>info@meridalefamilylaw.com</b></span>
</header>

<nav class="abs nav">
  <div class="brand" style="left:244px;top:10px">
    <div class="brand-dot"></div>
    <div class="brand-name">MERIDALE<br>FAMILY LAW</div>
  </div>
  <div class="nav-links">
    <span>Home</span><span>About Us</span><span>Our Services</span><span>Testimonials</span><span>FAQ</span><span>Blog</span><span>Contact Us</span>
  </div>
</nav>

<section class="abs hero" role="img" aria-label="Photo of three diverse, happy clients, two men and a woman, laughing together in a warm office">
  <div class="hero-card">
    <h1 class="heading">Changing the<br>Way People Divorce.</h1>
    <p>Efficient and positive family legal transitions<br>without costly, painful legal battles.</p>
    <div class="btn">Request A Free Consultation</div>
  </div>
</section>

<section class="abs panel panel-med">
  <h2 class="heading" style="left:278px">Meridale<br>Family Mediation</h2>
  <p style="left:280px">Our unique attorney-mediated process can deliver you and your family through divorce and into a healthy new life.</p>
  <div class="btn btn-dark" style="left:281px;top:193px">Read more</div>
</section>
<section class="abs panel panel-law">
  <h2 class="heading" style="left:51px">Meridale<br>Family Lawyer</h2>
  <p style="left:53px;top:123px;width:245px">Our attorneys are there when you need the protection of a mature, conscious advocate.</p>
  <div class="btn btn-dark" style="left:56px;top:190px">Read more</div>
</section>

<section class="abs about-text">
  <h2 class="heading">Meridale Family<br>Law &amp; Mediation LLC</h2>
  <p>Many people don't want to add unnecessary financial and emotional costs to their divorce, but they need professional help to ensure they come away with a good parenting plan and fair financial outcomes. For these people, we offer Meridale Family™ divorce mediation or, when necessary, a Meridale Family™ lawyer.</p>
</section>
<div class="btn btn-dark" style="left:355px;top:1272px;width:179px;height:34px;font-size:12.5px">Contact us today &nbsp;
  <svg width="26" height="8" viewBox="0 0 26 8"><path d="M0 4h24M20 1l4 3-4 3" stroke="#fff" fill="none" stroke-width="1.2"/></svg>
</div>
<div class="photo about-photo" role="img" aria-label="Photo of a smiling grey-haired woman in glasses at a friendly meeting"></div>

<section class="abs awards">
  <h2 class="heading">Legal Malpractice &amp; Appellate Lawyers with<br>Over Half a Century of Award-Winning Experience.</h2>
  <div class="badge" style="left:53px;width:115px;height:93px;background:#1f5a8f;border-radius:4px"></div>
  <div class="badge" style="left:185px;top:98px;width:70px;height:70px;background:#ef8a2c;border-radius:50%"></div>
  <div class="badge" style="left:264px;top:93px;width:118px;height:80px;background:#5a3e8c;border-radius:50%"></div>
  <div class="badge" style="left:406px;top:98px;width:82px;height:82px;background:#d9a429;border-radius:50%"></div>
  <div class="badge" style="left:505px;width:150px;height:93px;background:#f0f5fa"></div>
</section>

<h2 class="abs heading team-title">Attorneys<br>and Mediators</h2>
<div class="abs arrow" style="left:539px"><svg width="25" height="24"><path d="M14 7l-5 5 5 5" stroke="#fff" fill="none" stroke-width="1.6"/></svg></div>
<div class="abs arrow" style="left:572px"><svg width="25" height="24"><path d="M11 7l5 5-5 5" stroke="#fff" fill="none" stroke-width="1.6"/></svg></div>
<div class="photo attorney" style="left:242px" role="img" aria-label="Portrait photo of a smiling partner attorney"></div>
<div class="photo attorney" style="left:425px" role="img" aria-label="Portrait photo of a smiling partner attorney"></div>
<div class="abs att-name" style="left:232px">Daniel Ashcroft</div>
<div class="abs att-role" style="left:232px">Partner Attorney/Mediator</div>
<div class="abs att-name" style="left:415px">Daniel Ashcroft</div>
<div class="abs att-role" style="left:415px">Partner Attorney/Mediator</div>
<section class="abs quiz">
  <h2 class="heading">Mediation or Lawyer?</h2>
  <p>Our simple, free questionnaire can help you determine if you and your spouse are well suited for Meridale Family™ mediation, or if you may want legal representation for yourself.</p>
  <div class="btn">Take our free questionnaire</div>
</section>

<section class="abs call-box">
  <h2 class="heading">Get your<br>questions answered</h2>
  <div class="phone">(555) 014-2290</div>
  <div class="btn">Schedule a free information call</div>
</section>
<section class="abs form-box">
  <h2 class="heading">Request Your Free Consultation</h2>
  <div class="sub">Send us a message or call us at (555) 014-2290</div>
  <div class="field" style="left:48px;top:149px;width:165px;height:28px">Name*</div>
  <div class="field" style="left:228px;top:149px;width:166px;height:28px">Email*</div>
  <div class="field" style="left:48px;top:193px;width:346px;height:77px">Message*</div>
  <div class="btn send">Send message</div>
</section>
<div class="photo scene" role="img" aria-label="Photo of a parent and children walking across a golden mountain meadow under a blue sky"></div>
<div class="abs scene-caption">Divorce doesn't have to be<br>traumatic.</div>

<h2 class="abs heading video-title">Video : avoiding<br>harm to children in divorce</h2>
<div class="photo video" role="img" aria-label="Video thumbnail of a speaker talking about children in divorce">
  <div class="video-bar">Owen Talbot - How to avoid harm to children…</div>
  <div class="play"><svg width="40" height="30"><path d="M16 9l10 6-10 6z" fill="#fff"/></svg></div>
</div>
<div class="abs divider"></div>
<div class="brand firm-brand">
  <div class="brand-dot"></div>
  <div class="brand-name">MERIDALE<br>FAMILY LAW</div>
</div>
<div class="firm">
  <h3 class="abs heading">We are proud to serve your family</h3>
  <p class="abs">Meridale Family Law &amp; Mediation LLC currently serves the legal needs of Colorado residents (including same-sex and other alternative families) in Boulder County, Denver County, Broomfield County, Larimer County, Adams County, Weld County, and Jefferson County.</p>
</div>
<div class="btn btn-dark" style="left:627px;top:3151px;width:80px;height:23px;font-size:10px">Read more</div>

<section class="abs testimonials">
  <div class="ring" style="left:731px;top:14px;width:270px;height:270px"></div>
  <div class="ring" style="left:-112px;top:261px;width:352px;height:352px"></div>
  <h2 class="heading">Learn how our unique<br>mediation process has helped others</h2>
  <div class="btn outline-btn">View all testimonials</div>
  <div class="abs quote" style="left:290px;width:347px">"I am so grateful for my experience with Meridale Family Law &amp; Mediation. I learned so much about myself and my capacity to love, grieve, and heal. You were so great at facilitating our difficult conversations, helping both of us feel validated, and coaching us on how to work well with each other moving forward in our new co-parenting relationship."</div>
  <div class="abs quote" style="left:662px;width:337px">I really cannot thank you enough for all of your support and your excellent facilitation. I am almost certain that [my ex-husband] and I would not have been able to get through this so smoothly with anyone else. I love how you [grounded us at the] start [of] your sessions and it really helped me to step out of the fear and upset and focus on my boys and their well being. I will be forever grateful to you.</div>
  <div class="abs client" style="left:319px">Divorce mediation client</div>
  <div class="abs client" style="left:690px">Post-divorce mediation client</div>
</section>

<footer class="abs footer">
  <div class="f-title" style="left:272px">Quick Links</div>
  <ul class="f-list" style="left:272px"><li>Home</li><li>Our Story</li><li>Attorneys &amp; Mediators</li><li>Client Service Staff</li><li>Testimonials</li><li>FAQ</li></ul>
  <ul class="f-list" style="left:407px"><li>Blog</li><li>Contact Us</li><li>Resources</li><li>Meridale Family Mediation</li><li>Meridale Family Lawyer</li></ul>
  <div class="f-title" style="left:587px">Address</div>
  <div class="f-list" style="left:587px;top:91px;line-height:15.5px">Meridale Family Law &amp; Mediation LLC<br><span style="font-weight:400">1420 Alder Lane, Suite 2 Boulder,<br>Colorado 80302</span><br><br><span style="line-height:18px">Phone: <span style="font-weight:400">1+ (555) 014-2290</span><br>Mail: <span style="font-weight:400">info@meridalefamilylaw.com</span></span></div>
  <div class="f-title" style="left:837px">Subscribe with us</div>
  <div class="abs" style="left:819px;top:87px;width:164px;height:29px;background:#fff;border:1px solid #333"></div>
  <div class="btn" style="left:819px;top:122px;width:164px;height:29px;background:#2a2a2a;font-size:10.5px">Subscribe Now</div>
</footer>
<div class="abs copyright">© 2020 &nbsp;Meridale Family Law &amp; Mediation LLC. All Rights Reserved.</div>
<div class="abs social" style="left:911px"></div>
<div class="abs social" style="left:942px"></div>
<div class="abs social" style="left:973px;border-color:#d6402f"></div>

</body>
</html>
```